We are an integrated facilities management company.

We aggregate everything related to facilities maintenance. Repair-replacement of equipment and facility space materials from:
Asset gathering and tracking.
Vendor screening, contracting and management.
Service requirement development.
Work order processing and management.
Invoice reconciliation.
Vendor payment.
Reporting.
Capital equipment bids and project management.

Target Market(s)

Retail, hospitality, multi-family housing, long term healthcare.

Industry/Entity Type

Maintenance

Contact Information for Business Card

Professional and bold look. (see logo zip file)

Colors
3377b5
85abd2
cedeed

Requirements
Must have
• N/A
Nice to have
• N/A
Should not have
• N/A

```html
<!DOCTYPE html>
<html lang="en">
<head>
<meta charset="utf-8">
<title>Everloop Facility Partners – Business Card</title>
<link rel="stylesheet" href="https://fonts.googleapis.com/css2?family=Roboto:wght@400;500;700;900&display=swap">
<style>
  :root {
    --brand-blue: #3a78bd;
    --brand-blue-light: #85abd2;
    --brand-blue-pale: #cedeed;
    --ink: #1f1f1f;
    --ink-soft: #555a60;
    --paper: #ffffff;
    --backdrop: #e9ecef;
  }
  * { box-sizing: border-box; margin: 0; padding: 0; }
  html, body { width: 1200px; height: 900px; overflow: hidden; }
  body {
    background: var(--backdrop);
    font-family: "Roboto", Arial, sans-serif;
    color: var(--ink);
    position: relative;
  }
  .card {
    position: absolute;
    left: 250px;
    width: 700px;
    height: 400px;
    background: var(--paper);
    overflow: hidden;
    box-shadow: 0 6px 18px rgba(0,0,0,0.15);
  }
  .card--front { top: 30px; }
  .card--back { top: 470px; }

  /* Front */
  .edge-band { position: absolute; background: var(--brand-blue); }
  .edge-band--top { top: 0; left: 330px; right: 0; height: 14px; }
  .edge-band--bottom { bottom: 0; left: 0; width: 250px; height: 14px; }
  .edge-band--side { left: 0; top: 250px; bottom: 0; width: 12px; }

  .brand {
    position: absolute;
    display: flex;
    align-items: center;
    gap: 12px;
  }
  .brand__mark {
    width: 34px; height: 34px;
    background: var(--brand-blue);
    flex: none;
  }
  .brand__name {
    font-weight: 700;
    color: var(--brand-blue);
    text-transform: uppercase;
    line-height: 1.05;
    letter-spacing: 0.5px;
  }
  .card--front .brand { left: 40px; top: 120px; }
  .card--front .brand__name { font-size: 24px; }

  .divider { position: absolute; left: 0; top: 0; }

  .person { position: absolute; left: 380px; top: 100px; }
  .person__name { font-size: 30px; font-weight: 900; letter-spacing: 0.5px; text-transform: uppercase; }
  .person__title { font-size: 22px; color: var(--brand-blue); margin-top: 2px; }

  .contact-list { list-style: none; position: absolute; left: 380px; top: 200px; }
  .contact-list li {
    display: flex; align-items: center; gap: 14px;
    font-size: 24px; color: var(--ink); height: 38px;
  }
  .contact-list svg { width: 20px; height: 20px; fill: var(--brand-blue); flex: none; }

  /* Back */
  .card--back .header { position: absolute; top: 0; left: 0; right: 0; height: 95px; background: var(--paper); }
  .card--back .brand { right: 40px; top: 28px; }
  .card--back .brand__name { font-size: 26px; }
  .card--back .panel {
    position: absolute; top: 95px; left: 0; right: 0; height: 280px;
    background: var(--brand-blue);
    padding: 24px 34px;
  }
  .card--back .footer-strip { position: absolute; bottom: 0; left: 0; right: 0; height: 25px; background: var(--paper); }
  .services__lead { font-size: 20px; color: var(--paper); margin-bottom: 10px; }
  .services__list { list-style: none; font-size: 19px; line-height: 1.55; color: var(--ink); }
  .services__list li { display: inline; }
  .services__list li::before { content: "\2022\00a0"; }
  .services__list li::after { content: "\00a0\00a0"; }
</style>
</head>
<body>

<section class="card card--front" aria-label="Business card front">
  <div class="edge-band edge-band--top"></div>
  <div class="edge-band edge-band--side"></div>
  <div class="edge-band edge-band--bottom"></div>

  <div class="brand">
    <span class="brand__mark"></span>
    <span class="brand__name">Everloop<br>Facility Partners</span>
  </div>

  <svg class="divider" width="700" height="400" aria-hidden="true">
    <line x1="345" y1="130" x2="250" y2="300" stroke="#9aa0a6" stroke-width="2"/>
  </svg>

  <div class="person">
    <p class="person__name">Mara Dellow</p>
    <p class="person__title">Your Title Here</p>
  </div>

  <ul class="contact-list">
    <li>
      <svg viewBox="0 0 24 24" aria-hidden="true"><path d="M6.6 10.8a15.1 15.1 0 0 0 6.6 6.6l2.2-2.2a1 1 0 0 1 1-.25 11.4 11.4 0 0 0 3.6.57 1 1 0 0 1 1 1V20a1 1 0 0 1-1 1A17 17 0 0 1 3 4a1 1 0 0 1 1-1h3.5a1 1 0 0 1 1 1c0 1.25.2 2.45.57 3.57a1 1 0 0 1-.25 1z"/></svg>
      012 345 6789
    </li>
    <li>
      <svg viewBox="0 0 24 24" aria-hidden="true"><path d="M2 5h20v14H2z" opacity=".9"/><path d="M2 5l10 8 10-8" fill="none" stroke="#fff" stroke-width="2"/></svg>
      youremail@here.com
    </li>
    <li>
      <svg viewBox="0 0 24 24" aria-hidden="true"><circle cx="12" cy="12" r="10"/><path d="M2 12h20M12 2c3 3 3 17 0 20M12 2c-3 3-3 17 0 20" fill="none" stroke="#fff" stroke-width="1.5"/></svg>
      yourwebsitehere.com
    </li>
    <li>
      <svg viewBox="0 0 24 24" aria-hidden="true"><path d="M22 2L2 10l8 3 3 8z"/></svg>
      youraddresshere#123
    </li>
  </ul>
</section>

<section class="card card--back" aria-label="Business card back">
  <div class="header">
    <div class="brand">
      <span class="brand__mark"></span>
      <span class="brand__name">Everloop<br>Facility Partners</span>
    </div>
  </div>
  <div class="panel">
    <p class="services__lead">Repair-replacement of equipment and facility space materials from:</p>
    <ul class="services__list">
      <li>Asset gathering and tracking.</li>
      <li>contracting and management.</li>
      <li>Vendor screening.</li>
      <li>Service requirement development.</li>
      <li>Work order processing and management.</li>
      <li>Vendor payment.</li>
      <li>Reporting.</li>
      <li>Capital equipment bids and project management.</li>
      <li>Invoice reconciliation</li>
    </ul>
  </div>
  <div class="footer-strip"></div>
</section>

</body>
</html>
```